Luxury Customizable Mattress Company Needs a Business Card that WOWs

I need a unique business card design that makes people stop... look and think WOW.

We are a new mattress company with our very own line of customizable beds (mattress & base) called the Tessera Bed. The innovation of our mattress is that the entire product is built of smaller components... once put together its a complete bed. It can be cleaned from the inside out. And it's a mattress made to share with a partner. As people's sleep needs are different, one person may prefer a water bed and a softer mattress while their partner may prefer a warm memory foam mattress with a firmer feel. Now they dont need to compromise, as the Tessera Bed allows each sleeper to get exactly what they need. And they can each change the feel of their side of the bed anytime with a click of a button.
check www.Tesserabed-demo.com for more info (some pages do not work) Also check out our Plenix and Clipvane videos.

We also opened up a new facility where people can try out our beds... called the Quill Lounge. This is a secondary business but we would like to have a small logo on the TB business card to highlight it. (quilllounge-demo.com)

Content on card....
Logo: Tessera Bed logo
Name: Mirela Oshwin
Title: CEO & Sleep Enthusiast
Address: 4829 Talbrook Drive Mississauga ON L7X 3K2 Canada
Telephone: 416.555.0193 (place holder .. this # will change)
Email: mirela@tesserabed-demo.com
Web: www.tesserabed-demo.com

Small Logo: Quill Lounge Logo
web: quilllounge-demo.com

Design: bold and modern, the design has a concept, if possible a card people can use (to ensure they keep the card) Ie. Sleep positions or NFC chip or something interesting. I am open to ideas and printing on unique materials... like soft vinyl fabric.

Mattress Consumers
Married Couples
Couples

Health And Wellness

Logo: Tessera Bed logo
Name: Mirela Oshwin
Web: www.tesserabed-demo.com

SMALL Logo: Quill Lounge Logo
web: quilllounge-demo.com

• bold and modern, the design has a concept, if possible a card people can use (to ensure they keep the card)
• ** I LIKE THIS CONCEPT: http://example-cardgallery.test/uploads/2014/04/creative-business-card-sample-18.jpg
• And the DESIGN I thought of has a silhouette of a woman sleeping on top of front of card and if you flip the card over there's a silhouette of a man sleeping on the bottom of the back of the card. IF you put 2 cards together (back to front) it looks like they are sleeping together.
• INSIDE pull out card can be designed later.
• See our website and videos for images we've used in the past.
• We are open to new concepts, images, stories.
• Must be story / people driven. Mattress sales are driven by the idea of good sleep, solving sleep issues and making people happy.
• Just some examples.... adding a feature to the card like a Sleep positions chart or NFC chip or something interesting. I am open to ideas and printing on unique materials... like soft vinyl fabric.
• not dull in colour or concept

```html
<!DOCTYPE html>
<html lang="en">
<head>
<meta charset="utf-8">
<title>Tessera Bed — Business Card</title>
<link rel="stylesheet" href="https://fonts.googleapis.com/css2?family=Arimo:wght@400;700&family=Questrial&display=swap">
<style>
  :root {
    --stage: #e7e4df;
    --card-black: #050505;
    --band-grey: #b9b9bc;
    --rule-grey: #6f6f6f;
    --brand-blue: #2aa7e0;
    --deep-blue: #1a86c8;
    --logo-grey: #9a9a9a;
    --text-white: #f4f4f4;
  }
  * { box-sizing: border-box; margin: 0; padding: 0; }
  html, body { width: 1200px; height: 864px; overflow: hidden; }
  body {
    background: var(--stage);
    position: relative;
    font-family: "Arimo", Arial, sans-serif;
  }
  .card {
    position: absolute;
    top: 272px;
    width: 560px;
    height: 320px;
    background: var(--card-black);
    overflow: hidden;
    box-shadow: 0 6px 18px rgba(0,0,0,.25);
  }
  .card--front { left: 27px; }
  .card--back { left: 613px; }
  .card__band {
    position: absolute;
    left: 0; right: 0; bottom: 0;
    height: 58px;
    background: var(--band-grey);
  }
  .card__band::before {
    content: "";
    position: absolute;
    left: 0; right: 0; top: 6px;
    height: 4px;
    background: var(--card-black);
  }

  /* front */
  .brand {
    position: absolute;
    left: 26px; top: 92px;
    width: 190px;
    display: flex; flex-direction: column; align-items: flex-start; gap: 14px;
  }
  .brand__mark {
    width: 46px; height: 46px;
    background: var(--brand-blue);
  }
  .brand__name {
    font-family: "Questrial", sans-serif;
    font-size: 34px;
    line-height: 1.05;
    letter-spacing: 3px;
    text-transform: uppercase;
    color: var(--logo-grey);
  }
  .divider {
    position: absolute;
    left: 234px; top: 58px;
    width: 1px; height: 188px;
    background: var(--rule-grey);
  }
  .contact {
    position: absolute;
    left: 258px; top: 56px;
    color: var(--text-white);
  }
  .contact__name {
    font-family: "Questrial", sans-serif;
    font-size: 27px;
    color: var(--brand-blue);
    line-height: 1.05;
  }
  .contact__title { font-size: 15px; margin-top: 2px; }
  .contact__address { font-size: 14px; line-height: 1.3; margin-top: 18px; }
  .contact__list { list-style: none; margin-top: 16px; font-size: 14px; }
  .contact__item { display: flex; align-items: center; gap: 9px; height: 20px; }
  .contact__icon { width: 14px; height: 14px; flex: none; }

  /* back */
  .lounge {
    position: absolute;
    left: 0; right: 0; top: 40px;
    display: flex; flex-direction: column; align-items: center;
  }
  .lounge__mark {
    width: 118px; height: 118px;
    border-radius: 50%;
    background: var(--deep-blue);
  }
  .lounge__name {
    margin-top: 16px;
    font-weight: 700;
    font-size: 30px;
    letter-spacing: 4px;
    text-transform: uppercase;
    color: var(--deep-blue);
  }
  .lounge__web {
    margin-top: 8px;
    display: flex; align-items: center; gap: 14px;
    font-size: 15px;
    color: var(--brand-blue);
  }
  .lounge__rule { width: 96px; height: 1px; background: var(--rule-grey); }
</style>
</head>
<body>
  <section class="card card--front" aria-label="Card front">
    <div class="brand">
      <div class="brand__mark"></div>
      <div class="brand__name">Tessera Bed</div>
    </div>
    <div class="divider"></div>
    <div class="contact">
      <h1 class="contact__name">Mirela Oshwin</h1>
      <p class="contact__title">CEO &amp; Sleep Enthusiast</p>
      <p class="contact__address">4829 Talbrook Drive Mississauga<br>ON L7X 3K2 Canada</p>
      <ul class="contact__list">
        <li class="contact__item">
          <svg class="contact__icon" viewBox="0 0 14 14" aria-hidden="true"><rect width="14" height="14" fill="#2aa7e0"/><path d="M3 4c0 4 3 7 7 7l1-2-2-1-1 1C6.5 8.5 5.5 7.5 5 6l1-1-1-2z" fill="#050505"/></svg>
          <span>416.555.0193</span>
        </li>
        <li class="contact__item">
          <svg class="contact__icon" viewBox="0 0 14 14" aria-hidden="true"><rect width="14" height="14" fill="#2aa7e0"/><rect x="2.5" y="4" width="9" height="6" fill="none" stroke="#050505" stroke-width="1.2"/><path d="M2.5 4l4.5 3.5L11.5 4" fill="none" stroke="#050505" stroke-width="1.2"/></svg>
          <span>mirela@tesserabed-demo.com</span>
        </li>
        <li class="contact__item">
          <svg class="contact__icon" viewBox="0 0 14 14" aria-hidden="true"><rect width="14" height="14" fill="#2aa7e0"/><circle cx="7" cy="7" r="4.2" fill="none" stroke="#050505" stroke-width="1.2"/><path d="M2.8 7h8.4M7 2.8c-2 2.5-2 5.9 0 8.4M7 2.8c2 2.5 2 5.9 0 8.4" fill="none" stroke="#050505" stroke-width="1"/></svg>
          <span>www.tesserabed-demo.com</span>
        </li>
      </ul>
    </div>
    <div class="card__band"></div>
  </section>

  <section class="card card--back" aria-label="Card back">
    <div class="lounge">
      <div class="lounge__mark"></div>
      <div class="lounge__name">Quill Lounge</div>
      <div class="lounge__web">
        <span class="lounge__rule"></span>
        <span>quilllounge-demo.com</span>
        <span class="lounge__rule"></span>
      </div>
    </div>
    <div class="card__band"></div>
  </section>
</body>
</html>
```